Website redesign for Law Firm

Looking for someone experienced in Wordpress to redesign our existing website as part of a rebrand. The scope of the redesign includes:

1. Change logo and colours throughout to match new name and branding (minimal pink, mainly light and dark blue)
2. Redesign to focus of converison rate optimisation and modernisation. The focus is conveyancing and the call to action is Request an Instant Quote
3. Remove Meet the Leadership Team section from homepage
4. Remove Meet the Team section from About Us Page
5. Change ribbon to have Special Conditions and Blog as their own tabs, not a drop down under Resources
6. Include a Get a Free Quote section on the homepage similar to deedmarkhub.com.au, however does not require a State section. This calculator is to be coded into the final design and there will only be 3 different prices depending on what they choose

SLUG/Page stucture must stay the same for the final coded design.

Wanting something that is very clean and conversion rate optimised.

The existing website is tellerbyfirm.com.au. It is moving to harbourlinetitlelegal.com.au and changing name to Harbourline Title Legal.

The logo design files can be found here: https://files.examplevault.net/share/9kQpLr2XwTz7Bv4Nm8HcYd3Fs6Gj1?view=open

The colour codes and font name are included there also. You must use the correct colour codes from the logo. You can add a lighter blue to be the contract colour also. The pink colour is not to be a main colour it is just a feature colour to be used minimally. The dark blue from the background of the inverse (hex 192330) and a lighter blue are the main colours. Lots of white space and not all a dark background.

Examples of other websites in the industy

- https://keystepsettlements.com/
- https://www.deedmarkhub.com.au/
- https://truelinetransfers.com.au/

Target Market(s)

Professionals buying and selling property

Industry/Entity Type

Legal

Number of Pages Required

5+ page

Colors
0054AA
0677BA
7BADD7
CADEEF
E8F1F8

Requirements
Must have
• Wordpress and Elementor, Blue colour scheme.
Nice to have
• Get creative with the redesign/layout and focus on converison rate, especially above the fold. The existing layout does not need to stay the same
Should not have
• Minimal of the pink

```html
<!DOCTYPE html>
<html lang="en">
<head>
<meta charset="utf-8">
<title>Harbourline Title Legal – Website Pages</title>
<link href="https://fonts.googleapis.com/css2?family=Montserrat:wght@400;500;600;700;800&display=swap" rel="stylesheet">
<style>
:root{
  --navy:#192330;
  --navy-2:#22303f;
  --blue:#0054AA;
  --blue-2:#0677BA;
  --blue-3:#7BADD7;
  --blue-4:#CADEEF;
  --blue-5:#E8F1F8;
  --pink:#E5176E;
  --ink:#1d2733;
  --muted:#7a8694;
  --board:#eef0f3;
  --white:#ffffff;
}
*{margin:0;padding:0;box-sizing:border-box}
html,body{width:720px;height:1200px;overflow:hidden}
body{background:var(--board);font-family:'Montserrat',Arial,sans-serif;color:var(--ink);position:relative}
.page{position:absolute;background:var(--white);overflow:hidden;box-shadow:0 1px 4px rgba(25,35,48,.12);display:flex;flex-direction:column}
.home{left:12px;top:12px;width:212px;height:1168px}
.development{left:240px;top:12px;width:222px;height:838px}
.news{left:478px;top:12px;width:230px;height:336px}
.contact{left:478px;top:400px;width:230px;height:350px}
.about{left:478px;top:800px;width:230px;height:380px}

/* header */
.site-header{height:14px;background:var(--navy);display:flex;align-items:center;padding:0 6px;gap:6px;flex-shrink:0}
.logo{color:var(--white);font-weight:700;font-size:4.6px;display:flex;align-items:center;gap:2px;letter-spacing:.2px}
.logo-mark{width:5px;height:5px;background:var(--blue-3);display:inline-block}
.nav{display:flex;gap:4px;margin-left:auto;font-size:3px;color:var(--blue-4)}
.btn{background:var(--pink);color:var(--white);font-size:3.2px;font-weight:600;padding:1.6px 4px;border-radius:1px;white-space:nowrap}
.btn.blue{background:var(--blue)}
.btn.big{font-size:4px;padding:2.4px 6px}

.page-banner{height:40px;background:linear-gradient(120deg,var(--navy) 0%,var(--navy-2) 60%,#2d3e52 100%);display:flex;align-items:center;justify-content:center;color:var(--white);font-weight:700;font-size:6.5px;letter-spacing:.4px;flex-shrink:0}

.photo{border-radius:1.5px;background:linear-gradient(135deg,var(--blue-4),var(--blue-3))}
.photo.warm{background:linear-gradient(135deg,#d9cbbd,#9fb2c4)}
.photo.dark{background:linear-gradient(135deg,#3c4c5e,#1f2b38)}
.photo.city{background:linear-gradient(160deg,#a9c6e0,#5c7d9c)}

.eyebrow{font-size:3.4px;color:var(--pink);font-weight:600;letter-spacing:.3px}
.title{font-weight:800;font-size:6.2px;line-height:1.2;color:var(--navy);letter-spacing:.2px}
.title.center{text-align:center}
.body{font-size:3.3px;line-height:1.45;color:var(--muted)}
.body.center{text-align:center}

.dark-band{background:var(--navy);color:var(--white);display:flex;flex-direction:column;align-items:center;justify-content:center;gap:3px;flex-shrink:0}
.dark-band .title{color:var(--white)}
.dark-band .body{color:var(--blue-4)}

.site-footer{margin-top:auto;background:var(--navy);display:grid;grid-template-columns:1.1fr 1fr 1fr 1fr;gap:5px;padding:10px 8px;color:var(--blue-4);flex-shrink:0}
.site-footer h6{font-size:3.6px;color:var(--white);font-weight:700;margin-bottom:3px}
.site-footer p{font-size:3px;line-height:1.7}
.footer-input{display:block;height:5px;background:var(--navy-2);border:.4px solid var(--blue-3);margin-top:2px;border-radius:1px}
.copyright{grid-column:1/-1;border-top:.4px solid #34455a;padding-top:4px;font-size:2.8px;text-align:center}

.icon-circle{width:12px;height:12px;border-radius:50%;background:var(--blue-5);display:flex;align-items:center;justify-content:center;flex-shrink:0}
.icon-circle svg{width:7px;height:7px}

/* HOME */
.hero{height:132px;padding:10px 8px;display:grid;grid-template-columns:1fr 88px;gap:6px;background:linear-gradient(180deg,var(--white),var(--blue-5))}
.hero h1{font-weight:800;font-size:8.6px;line-height:1.2;color:var(--navy);margin:3px 0 4px}
.hero h1 span{color:var(--blue-2)}
.hero .photo{height:74px}
.hero-copy .btn{display:inline-block;margin-top:5px}
.stats{grid-column:1/-1;display:flex;gap:5px}
.stat{flex:1;background:var(--white);border:.5px solid var(--blue-4);border-radius:2px;padding:4px;display:flex;gap:3px;align-items:center}
.stat b{font-size:6px;color:var(--blue)}
.stat span{font-size:2.8px;color:var(--muted);line-height:1.3}

.quote{height:135px;padding:10px 8px;display:grid;grid-template-columns:1fr 86px;gap:7px;align-items:start}
.quote .title{margin:3px 0 4px}
.quote .photo{height:66px}
.quote-form{grid-column:1/-1;background:var(--blue-5);border-radius:2px;padding:5px;display:flex;gap:4px;align-items:center}
.field{flex:1;height:8px;background:var(--white);border:.4px solid var(--blue-4);border-radius:1px;font-size:2.8px;color:var(--muted);padding-left:2px;display:flex;align-items:center}

.testimonials{height:62px}
.quotes-row{display:flex;gap:4px}
.quote-card{width:55px;height:20px;background:var(--navy-2);border-radius:2px;padding:3px;font-size:2.8px;color:var(--blue-4);line-height:1.4}

.tools,.services{height:112px;padding:10px 8px;display:flex;flex-direction:column;align-items:center;gap:5px}
.tool-row,.service-row{display:flex;gap:5px;width:100%}
.tool{flex:1;display:flex;flex-direction:column;align-items:center;gap:3px;text-align:center}
.tool .icon-circle{width:18px;height:18px}
.tool b{font-size:3.6px;color:var(--navy)}
.tool .btn{font-size:2.8px}
.service{flex:1;display:flex;flex-direction:column;gap:3px}
.service .photo{height:40px}
.service b{font-size:3.6px;color:var(--navy)}

.cta-band{height:55px;display:grid;grid-template-columns:1fr 70px;background:var(--blue-5)}
.cta-band .cta-copy{padding:9px 8px;display:flex;flex-direction:column;gap:4px;align-items:flex-start}
.cta-band .photo{border-radius:0}

.help{height:135px;padding:10px 8px;display:flex;flex-direction:column;align-items:center;gap:5px}
.help-grid{display:grid;grid-template-columns:repeat(3,1fr);gap:5px;width:100%}
.help-card{border:.5px solid var(--blue-4);border-radius:2px;padding:4px;display:flex;flex-direction:column;align-items:center;gap:2px;text-align:center;height:42px}
.help-card b{font-size:3.4px;color:var(--navy)}

.partners{height:38px;background:var(--navy);display:flex;align-items:center;justify-content:space-around;padding:0 8px}
.partner{width:34px;height:11px;background:var(--white);border-radius:1.5px}

.blog{height:128px;padding:10px 8px;display:flex;flex-direction:column;gap:5px}
.blog-row{display:flex;gap:5px}
.post{flex:1;display:flex;flex-direction:column;gap:3px}
.post .photo{height:44px}
.post b{font-size:3.4px;color:var(--navy);line-height:1.3}

/* DEVELOPMENT */
.dev-intro{height:118px;padding:10px 8px;display:grid;grid-template-columns:92px 1fr;gap:7px;align-items:center}
.dev-intro .photo{height:80px}
.dev-intro .title{margin-bottom:4px}
.dev-intro .btn{display:inline-block;margin-top:4px}
.ticks{height:120px;padding:6px 10px;display:grid;grid-template-columns:1fr 1fr;gap:5px 8px;align-content:center;background:var(--blue-5)}
.tick{display:flex;gap:3px;align-items:center;font-size:3.2px;color:var(--ink)}
.tick svg{width:6px;height:6px;flex-shrink:0}
.want-band{height:62px}
.difference{height:108px;padding:10px 8px;display:grid;grid-template-columns:1fr 88px;gap:7px;align-items:center}
.difference .photo{height:72px}
.difference .title{margin-bottom:4px}
.icon-cards{height:56px;display:flex;gap:5px;padding:0 8px;align-items:center}
.icon-card{flex:1;height:40px;border:.5px solid var(--blue-4);border-radius:2px;display:flex;flex-direction:column;align-items:center;justify-content:center;gap:3px;font-size:3px;color:var(--navy);font-weight:600;text-align:center}
.proven{height:100px;background:var(--navy);padding:10px 8px;display:flex;flex-direction:column;align-items:center;gap:6px}
.proven .title{color:var(--white)}
.proven-row{display:flex;gap:5px;width:100%}
.proven-card{flex:1;height:46px;background:var(--white);border-radius:2px;padding:4px;display:flex;flex-direction:column;gap:2px;align-items:center;text-align:center}
.proven-card b{font-size:3.2px;color:var(--navy)}
.dev-text{height:92px;padding:12px 12px;display:flex;flex-direction:column;align-items:center;gap:5px}
.need{height:34px;display:flex;align-items:center;justify-content:center;flex-direction:column;gap:3px;background:var(--blue-5)}

/* NEWS */
.news-grid{padding:9px 8px 4px;display:grid;grid-template-columns:repeat(3,1fr);gap:6px 5px}
.news-item{display:flex;flex-direction:column;gap:2px}
.news-item .photo{height:34px}
.news-item b{font-size:3.2px;color:var(--navy);line-height:1.3}
.news-item span{font-size:2.6px;color:var(--muted)}
.pagination{display:flex;gap:3px;justify-content:center;padding:4px 0 8px}
.pagination i{width:5px;height:5px;border-radius:50%;background:var(--blue-4);display:block}
.pagination i.on{background:var(--blue)}

/* CONTACT */
.touch{padding:8px 8px 4px;display:flex;flex-direction:column;align-items:center;gap:5px}
.touch-row{display:flex;gap:5px;width:100%}
.touch-card{flex:1;border:.5px solid var(--blue-4);border-radius:2px;padding:4px;display:flex;flex-direction:column;align-items:center;gap:2px;font-size:3px;color:var(--navy);text-align:center}
.touch-card b{font-size:3.3px}
.contact-form{margin:4px 8px;padding:6px;background:var(--blue-5);border-radius:2px;display:grid;grid-template-columns:1fr 1fr;gap:4px}
.contact-form .wide{grid-column:1/-1;height:16px;align-items:flex-start;padding-top:2px}
.contact-form .btn{justify-self:start}
.map{margin:4px 0 0;height:72px;border-radius:0;background:linear-gradient(135deg,#dfe8df,#c9dbe9 60%,#a9c6e0)}

/* ABOUT */
.about-intro{height:128px;padding:10px 8px;display:grid;grid-template-columns:96px 1fr;gap:7px;align-items:center}
.about-intro .photo{height:96px}
.about-intro .title{margin-bottom:4px}
.about-icons{height:58px;display:flex;gap:5px;padding:0 8px;align-items:center}
.need-about{height:48px}
</style>
</head>
<body>

<!-- Home page -->
<section class="page home">
  <header class="site-header">
    <div class="logo"><span class="logo-mark"></span>Harbourline Title Legal</div>
    <nav class="nav"><span>About</span><span>Services</span><span>Blog</span><span>Contact</span></nav>
    <span class="btn">Get a Quote</span>
  </header>
  <div class="hero">
    <div class="hero-copy">
      <div class="eyebrow">FIXED FEE CONVEYANCING</div>
      <h1>BRISBANE CONVEYANCING <span>WITHOUT THE HIDDEN COSTS</span></h1>
      <p class="body">Clear fixed fees and expert guidance from contract to settlement day.</p>
      <span class="btn big">Request an Instant Quote</span>
    </div>
    <div class="photo warm" role="img" aria-label="Photo of a couple holding keys to their new home"></div>
    <div class="stats">
      <div class="stat"><b>5k+</b><span>Happy clients settled</span></div>
      <div class="stat"><b>4.9</b><span>Average client rating</span></div>
      <div class="stat"><b>100%</b><span>Fixed fee pricing</span></div>
    </div>
  </div>
  <div class="quote">
    <div>
      <div class="eyebrow">GET A FREE QUOTE</div>
      <h2 class="title">INSTANT CONVEYANCING QUOTE IN 60 SECOND</h2>
      <p class="body">Tell us if you are buying or selling and see your price straight away.</p>
    </div>
    <div class="photo warm" role="img" aria-label="Photo of a smiling family at home"></div>
    <div class="quote-form">
      <span class="field">Buying / Selling</span>
      <span class="field">Property type</span>
      <span class="btn">Get Quote</span>
    </div>
  </div>
  <div class="dark-band testimonials">
    <h2 class="title">WHAT OUR CLIENT SAYS</h2>
    <div class="quotes-row">
      <div class="quote-card">Quick, friendly and clear from start to finish.</div>
      <div class="quote-card">Settlement was smooth and stress free.</div>
      <div class="quote-card">Great value and always kept us updated.</div>
    </div>
  </div>
  <div class="tools">
    <h2 class="title center">FREE TOOLS FOR BUYERS &amp; SELLERS</h2>
    <p class="body center">Simple guides and calculators to plan your move.</p>
    <div class="tool-row">
      <div class="tool"><span class="icon-circle"><svg viewBox="0 0 10 10"><rect x="2" y="1" width="6" height="8" rx="1" fill="none" stroke="#0054AA" stroke-width="1"/><path d="M3.5 3h3M3.5 5h3M3.5 7h2" stroke="#0054AA" stroke-width=".8"/></svg></span><b>Stamp Duty</b><span class="btn blue">Calculate</span></div>
      <div class="tool"><span class="icon-circle"><svg viewBox="0 0 10 10"><path d="M1.5 5L5 2l3.5 3v3.5h-7z" fill="none" stroke="#0054AA" stroke-width="1"/></svg></span><b>Buyer Guide</b><span class="btn blue">Download</span></div>
      <div class="tool"><span class="icon-circle"><svg viewBox="0 0 10 10"><path d="M2 5.2l2 2 4-4.4" fill="none" stroke="#0054AA" stroke-width="1.1"/></svg></span><b>Seller Checklist</b><span class="btn blue">Download</span></div>
    </div>
  </div>
  <div class="services">
    <h2 class="title center">OUR SERVICES</h2>
    <div class="service-row">
      <div class="service"><div class="photo city" role="img" aria-label="Photo of a suburban house"></div><b>Buying Property</b><p class="body">Contract review and settlement.</p></div>
      <div class="service"><div class="photo city" role="img" aria-label="Photo of a modern home exterior"></div><b>Selling Property</b><p class="body">Contracts prepared fast.</p></div>
      <div class="service"><div class="photo city" role="img" aria-label="Photo of a development site"></div><b>Development</b><p class="body">Off the plan and projects.</p></div>
    </div>
  </div>
  <div class="cta-band">
    <div class="cta-copy">
      <h2 class="title">WOULD YOU LIKE TO GET STARTED WITH US?</h2>
      <span class="btn">Request a Quote</span>
    </div>
    <div class="photo warm" role="img" aria-label="Photo of a lawyer meeting a client"></div>
  </div>
  <div class="help">
    <h2 class="title center">HOW CAN WE HELP YOU?</h2>
    <div class="help-grid">
      <div class="help-card"><span class="icon-circle"><svg viewBox="0 0 10 10"><path d="M1.5 5L5 2l3.5 3v3.5h-7z" fill="none" stroke="#0054AA" stroke-width="1"/></svg></span><b>Buying</b><p class="body">Fixed fee buyer help.</p></div>
      <div class="help-card"><span class="icon-circle"><svg viewBox="0 0 10 10"><path d="M2 5.2l2 2 4-4.4" fill="none" stroke="#0054AA" stroke-width="1.1"/></svg></span><b>Selling</b><p class="body">Contracts made simple.</p></div>
      <div class="help-card"><span class="icon-circle"><svg viewBox="0 0 10 10"><rect x="2" y="2" width="6" height="6" fill="none" stroke="#0054AA" stroke-width="1"/></svg></span><b>Transfers</b><p class="body">Title changes handled.</p></div>
      <div class="help-card"><span class="icon-circle"><svg viewBox="0 0 10 10"><circle cx="5" cy="5" r="3" fill="none" stroke="#0054AA" stroke-width="1"/></svg></span><b>Off the Plan</b><p class="body">New build purchases.</p></div>
      <div class="help-card"><span class="icon-circle"><svg viewBox="0 0 10 10"><path d="M2 8V3h6v5" fill="none" stroke="#0054AA" stroke-width="1"/></svg></span><b>Commercial</b><p class="body">Business premises.</p></div>
      <div class="help-card"><span class="icon-circle"><svg viewBox="0 0 10 10"><path d="M2 5h6M5 2v6" stroke="#0054AA" stroke-width="1"/></svg></span><b>Special Conditions</b><p class="body">Clauses drafted right.</p></div>
    </div>
  </div>
  <div class="partners">
    <span class="partner"></span><span class="partner"></span><span class="partner"></span><span class="partner"></span>
  </div>
  <div class="blog">
    <h2 class="title center">LATEST FROM BLOG</h2>
    <div class="blog-row">
      <div class="post"><div class="photo city" role="img" aria-label="Photo of a city skyline"></div><b>First Home Buyer Tips</b><p class="body">What to check first.</p></div>
      <div class="post"><div class="photo warm" role="img" aria-label="Photo of contract signing"></div><b>Cooling Off Explained</b><p class="body">Your rights as buyer.</p></div>
      <div class="post"><div class="photo city" role="img" aria-label="Photo of a home for sale"></div><b>Selling in Winter</b><p class="body">Timing your sale.</p></div>
    </div>
  </div>
  <footer class="site-footer">
    <div><div class="logo"><span class="logo-mark"></span>Harbourline</div><p>Property law made clear.</p></div>
    <div><h6>Quick Links</h6><p>About Us</p><p>Services</p><p>Blog</p></div>
    <div><h6>Contact Us</h6><p>Mon–Fri 9–5</p><p>Suite 4, Harbour Rd</p></div>
    <div><h6>Newsletter</h6><p>Property updates</p><span class="footer-input"></span></div>
    <div class="copyright">© Harbourline Title Legal. All rights reserved.</div>
  </footer>
</section>

<!-- Property development page -->
<section class="page development">
  <header class="site-header">
    <div class="logo"><span class="logo-mark"></span>Harbourline</div>
    <nav class="nav"><span>About</span><span>Services</span><span>Blog</span></nav>
    <span class="btn">Get a Quote</span>
  </header>
  <div class="page-banner">PROPERTY DEVELOPMENT</div>
  <div class="dev-intro">
    <div class="photo dark" role="img" aria-label="Photo of a developer reviewing plans"></div>
    <div>
      <h2 class="title">PROPERTY DEVELOPMENT LAWYERS BRISBANE</h2>
      <p class="body">We guide developers through every legal step, from site purchase and approvals to sales contracts and final settlement.</p>
      <span class="btn">Request a Quote</span>
    </div>
  </div>
  <div class="ticks">
    <div class="tick"><svg viewBox="0 0 10 10"><circle cx="5" cy="5" r="5" fill="#0054AA"/><path d="M2.8 5.2l1.6 1.6 3-3.4" fill="none" stroke="#fff" stroke-width="1"/></svg>Site acquisition advice</div>
    <div class="tick"><svg viewBox="0 0 10 10"><circle cx="5" cy="5" r="5" fill="#0054AA"/><path d="M2.8 5.2l1.6 1.6 3-3.4" fill="none" stroke="#fff" stroke-width="1"/></svg>Off the plan contracts</div>
    <div class="tick"><svg viewBox="0 0 10 10"><circle cx="5" cy="5" r="5" fill="#0054AA"/><path d="M2.8 5.2l1.6 1.6 3-3.4" fill="none" stroke="#fff" stroke-width="1"/></svg>Joint venture agreements</div>
    <div class="tick"><svg viewBox="0 0 10 10"><circle cx="5" cy="5" r="5" fill="#0054AA"/><path d="M2.8 5.2l1.6 1.6 3-3.4" fill="none" stroke="#fff" stroke-width="1"/></svg>Community titles schemes</div>
    <div class="tick"><svg viewBox="0 0 10 10"><circle cx="5" cy="5" r="5" fill="#0054AA"/><path d="M2.8 5.2l1.6 1.6 3-3.4" fill="none" stroke="#fff" stroke-width="1"/></svg>Subdivision and approvals</div>
    <div class="tick"><svg viewBox="0 0 10 10"><circle cx="5" cy="5" r="5" fill="#0054AA"/><path d="M2.8 5.2l1.6 1.6 3-3.4" fill="none" stroke="#fff" stroke-width="1"/></svg>Finance and securities</div>
    <div class="tick"><svg viewBox="0 0 10 10"><circle cx="5" cy="5" r="5" fill="#0054AA"/><path d="M2.8 5.2l1.6 1.6 3-3.4" fill="none" stroke="#fff" stroke-width="1"/></svg>Sales and settlements</div>
    <div class="tick"><svg viewBox="0 0 10 10"><circle cx="5" cy="5" r="5" fill="#0054AA"/><path d="M2.8 5.2l1.6 1.6 3-3.4" fill="none" stroke="#fff" stroke-width="1"/></svg>Dispute resolution</div>
  </div>
  <div class="dark-band want-band">
    <h2 class="title">WANT TO KNOW MORE?</h2>
    <p class="body">Speak with our development team today.</p>
    <span class="btn">Contact Us</span>
  </div>
  <div class="difference">
    <div>
      <h2 class="title">THE HARBOURLINE TITLE LEGAL DIFFERENCE</h2>
      <p class="body">Practical advice, fast replies and fixed fees so your project stays on time and on budget.</p>
    </div>
    <div class="photo warm" role="img" aria-label="Photo of a hand signing a contract"></div>
  </div>
  <div class="icon-cards">
    <div class="icon-card"><span class="icon-circle"><svg viewBox="0 0 10 10"><path d="M2 5.2l2 2 4-4.4" fill="none" stroke="#0054AA" stroke-width="1.1"/></svg></span>Fixed Fees</div>
    <div class="icon-card"><span class="icon-circle"><svg viewBox="0 0 10 10"><circle cx="5" cy="5" r="3" fill="none" stroke="#0054AA" stroke-width="1"/></svg></span>Fast Replies</div>
    <div class="icon-card"><span class="icon-circle"><svg viewBox="0 0 10 10"><rect x="2" y="2" width="6" height="6" fill="none" stroke="#0054AA" stroke-width="1"/></svg></span>Expert Team</div>
    <div class="icon-card"><span class="icon-circle"><svg viewBox="0 0 10 10"><path d="M1.5 5L5 2l3.5 3v3.5h-7z" fill="none" stroke="#0054AA" stroke-width="1"/></svg></span>Local Focus</div>
  </div>
  <div class="proven">
    <h2 class="title center">PROVEN TRACK RECORD OF ASSISTING DEVELOPERS BY</h2>
    <div class="proven-row">
      <div class="proven-card"><span class="icon-circle"><svg viewBox="0 0 10 10"><path d="M2 8V3h6v5" fill="none" stroke="#0054AA" stroke-width="1"/></svg></span><b>Planning</b><p class="body">Early legal checks.</p></div>
      <div class="proven-card"><span class="icon-circle"><svg viewBox="0 0 10 10"><path d="M2 5h6M5 2v6" stroke="#0054AA" stroke-width="1"/></svg></span><b>Structuring</b><p class="body">Sound deal setup.</p></div>
      <div class="proven-card"><span class="icon-circle"><svg viewBox="0 0 10 10"><path d="M2 5.2l2 2 4-4.4" fill="none" stroke="#0054AA" stroke-width="1.1"/></svg></span><b>Selling</b><p class="body">Contracts ready.</p></div>
    </div>
  </div>
  <div class="dev-text">
    <h2 class="title center">BRISBANE PROPERTY DEVELOPMENT LAWYERS</h2>
    <p class="body center">From small subdivisions to large projects, our lawyers give clear advice at every stage so you can build with confidence and sell on schedule.</p>
  </div>
  <div class="need">
    <h2 class="title">NEED ASSISTANCE</h2>
    <span class="btn">Call Us Today</span>
  </div>
  <footer class="site-footer">
    <div><div class="logo"><span class="logo-mark"></span>Harbourline</div><p>Property law made clear.</p></div>
    <div><h6>Quick Links</h6><p>About Us</p><p>Services</p></div>
    <div><h6>Contact Us</h6><p>Mon–Fri 9–5</p><p>Suite 4, Harbour Rd</p></div>
    <div><h6>Newsletter</h6><span class="footer-input"></span></div>
    <div class="copyright">© Harbourline Title Legal.</div>
  </footer>
</section>

<!-- News page -->
<section class="page news">
  <header class="site-header">
    <div class="logo"><span class="logo-mark"></span>Harbourline</div>
    <nav class="nav"><span>About</span><span>Blog</span></nav>
    <span class="btn">Get a Quote</span>
  </header>
  <div class="page-banner">NEWS &amp; KNOWLEDGE</div>
  <div class="news-grid">
    <div class="news-item"><div class="photo city" role="img" aria-label="Photo of a residential street"></div><b>Buying at Auction</b><span>Read more</span></div>
    <div class="news-item"><div class="photo warm" role="img" aria-label="Photo of documents on a desk"></div><b>Building Inspections</b><span>Read more</span></div>
    <div class="news-item"><div class="photo city" role="img" aria-label="Photo of apartment towers"></div><b>Body Corporate Basics</b><span>Read more</span></div>
    <div class="news-item"><div class="photo warm" role="img" aria-label="Photo of a family home"></div><b>Settlement Day Guide</b><span>Read more</span></div>
    <div class="news-item"><div class="photo city" role="img" aria-label="Photo of a city skyline"></div><b>Market Update</b><span>Read more</span></div>
    <div class="news-item"><div class="photo dark" role="img" aria-label="Photo of a meeting room"></div><b>Finance Clauses</b><span>Read more</span></div>
    <div class="news-item"><div class="photo city" role="img" aria-label="Photo of a new estate"></div><b>Off the Plan Risks</b><span>Read more</span></div>
    <div class="news-item"><div class="photo warm" role="img" aria-label="Photo of house keys"></div><b>Title Searches</b><span>Read more</span></div>
    <div class="news-item"><div class="photo city" role="img" aria-label="Photo of a townhouse row"></div><b>Selling Tips</b><span>Read more</span></div>
  </div>
  <div class="pagination"><i class="on"></i><i></i><i></i><i></i></div>
  <footer class="site-footer">
    <div><div class="logo"><span class="logo-mark"></span>Harbourline</div></div>
    <div><h6>Quick Links</h6><p>About Us</p></div>
    <div><h6>Contact Us</h6><p>Mon–Fri 9–5</p></div>
    <div><h6>Newsletter</h6><span class="footer-input"></span></div>
  </footer>
</section>

<!-- Contact page -->
<section class="page contact">
  <header class="site-header">
    <div class="logo"><span class="logo-mark"></span>Harbourline</div>
    <nav class="nav"><span>About</span><span>Blog</span></nav>
    <span class="btn">Get a Quote</span>
  </header>
  <div class="page-banner">CONTACT US</div>
  <div class="touch">
    <h2 class="title center">GET IN TOUCH WITH US</h2>
    <div class="touch-row">
      <div class="touch-card"><span class="icon-circle"><svg viewBox="0 0 10 10"><path d="M3 1.5l1.4 2-1 1c.5 1 1.2 1.7 2.1 2.1l1-1 2 1.4-1 1.5C5 8 2 5 1.5 2.5z" fill="#0054AA"/></svg></span><b>Call Us</b>(07) 5550 1234</div>
      <div class="touch-card"><span class="icon-circle"><svg viewBox="0 0 10 10"><rect x="1.5" y="2.5" width="7" height="5" fill="none" stroke="#0054AA" stroke-width="1"/><path d="M1.5 2.5L5 5.5l3.5-3" fill="none" stroke="#0054AA" stroke-width="1"/></svg></span><b>Email Us</b>hello@harbourline.au</div>
      <div class="touch-card"><span class="icon-circle"><svg viewBox="0 0 10 10"><path d="M5 9S2 5.8 2 4a3 3 0 016 0c0 1.8-3 5-3 5z" fill="#0054AA"/><circle cx="5" cy="4" r="1" fill="#fff"/></svg></span><b>Visit Us</b>Suite 4, Harbour Rd</div>
    </div>
  </div>
  <form class="contact-form">
    <span class="field">Name</span><span class="field">Email</span>
    <span class="field wide">Message</span>
    <span class="btn">Send Message</span>
  </form>
  <div class="photo map" role="img" aria-label="Map showing the office location"></div>
  <footer class="site-footer">
    <div><div class="logo"><span class="logo-mark"></span>Harbourline</div></div>
    <div><h6>Quick Links</h6><p>About Us</p></div>
    <div><h6>Contact Us</h6><p>Mon–Fri 9–5</p></div>
    <div><h6>Newsletter</h6><span class="footer-input"></span></div>
  </footer>
</section>

<!-- About page -->
<section class="page about">
  <header class="site-header">
    <div class="logo"><span class="logo-mark"></span>Harbourline</div>
    <nav class="nav"><span>About</span><span>Blog</span></nav>
    <span class="btn">Get a Quote</span>
  </header>
  <div class="page-banner">ABOUT US</div>
  <div class="about-intro">
    <div class="photo dark" role="img" aria-label="Photo of the legal team at the office"></div>
    <div>
      <h2 class="title">WE ARE HARBOURLINE TITLE LEGAL</h2>
      <p class="body">A Brisbane property law firm helping buyers, sellers and developers with clear fixed fee advice and friendly service from first call to settlement.</p>
    </div>
  </div>
  <div class="about-icons">
    <div class="icon-card"><span class="icon-circle"><svg viewBox="0 0 10 10"><path d="M2 5.2l2 2 4-4.4" fill="none" stroke="#0054AA" stroke-width="1.1"/></svg></span>Trusted</div>
    <div class="icon-card"><span class="icon-circle"><svg viewBox="0 0 10 10"><circle cx="5" cy="5" r="3" fill="none" stroke="#0054AA" stroke-width="1"/></svg></span>Fast</div>
    <div class="icon-card"><span class="icon-circle"><svg viewBox="0 0 10 10"><rect x="2" y="2" width="6" height="6" fill="none" stroke="#0054AA" stroke-width="1"/></svg></span>Fixed Fees</div>
    <div class="icon-card"><span class="icon-circle"><svg viewBox="0 0 10 10"><path d="M1.5 5L5 2l3.5 3v3.5h-7z" fill="none" stroke="#0054AA" stroke-width="1"/></svg></span>Local</div>
  </div>
  <div class="need need-about">
    <h2 class="title">NEED ASSISTANCE</h2>
    <span class="btn">Call Us Today</span>
  </div>
  <footer class="site-footer">
    <div><div class="logo"><span class="logo-mark"></span>Harbourline</div><p>Property law made clear.</p></div>
    <div><h6>Quick Links</h6><p>About Us</p><p>Services</p></div>
    <div><h6>Contact Us</h6><p>Mon–Fri 9–5</p></div>
    <div><h6>Newsletter</h6><span class="footer-input"></span></div>
    <div class="copyright">© Harbourline Title Legal.</div>
  </footer>
</section>

</body>
</html>
```